Pull Up Banner Design 85cm X200cm

The pull up banner is intended for branding and services awareness purposes, and to be used at exhibition and conference. Please refer to the websites below for more information
1. https://www.brivanta.online/
2. https://www.brivanta.online/landing-page
3. https://blog.brivanta.online/faq-for-client/
4. https://blog.brivanta.online/faq-for-advisor/

Ideally, the banner will lead potential users both young entrepreneurs and online business owners (as clients) to Brivanta marketplace, and also professional services providers like accountants and finance advisors and consultants (as advisors) to sign up with the platform. (Like PixelHarbor marketplace)

Target Market(s)

Business users and accountants aged between 25 to 44 yrs old

Requirements
Must have
• website address (www.brivanta.online)
• and
• company logo "Brivanta" as attached

```html
<!DOCTYPE html>
<html lang="en">
<head>
<meta charset="utf-8">
<title>Brivanta – Pull Up Banner</title>
<link href="https://fonts.googleapis.com/css2?family=Bebas+Neue&family=Montserrat:wght@700&family=Roboto:wght@400&display=swap" rel="stylesheet">
<style>
  :root{
    --stage:#d9d9db;
    --paper:#f3f3f5;
    --brand-blue:#1a73c2;
    --ink-grey:#4a4a4c;
    --tab-grey:#5a5a5c;
    --curve-grey:#c8c8cc;
    --teal:#5fc3c0;
    --white:#ffffff;
  }
  *{margin:0;padding:0;box-sizing:border-box}
  html,body{width:1200px;height:991px;overflow:hidden;background:var(--stage)}
  .banner{position:absolute;left:398px;top:20px;width:404px;height:951px;background:var(--paper);overflow:hidden;box-shadow:0 4px 14px rgba(0,0,0,.25);font-family:"Roboto",Arial,sans-serif}
  .hero-photo{position:absolute;left:0;top:0;width:404px;height:320px;background:radial-gradient(circle at 78% 40%,#c7a58c 0,#8d6a55 30%,transparent 60%),linear-gradient(160deg,#6b5a4a 0%,#4a3d34 45%,#7a6656 100%)}
  .hero-curve{position:absolute;left:0;top:260px;width:404px;height:80px}
  .headline{position:absolute;left:19px;top:66px;font-family:"Bebas Neue",Impact,sans-serif;font-weight:400;font-size:32px;line-height:39px;color:var(--white);letter-spacing:.5px}
  .brand{position:absolute;left:0;width:404px;top:330px;text-align:center}
  .brand-dot{width:64px;height:64px;border-radius:50%;background:var(--brand-blue);margin:0 auto}
  .brand-name{font-family:"Montserrat",Arial,sans-serif;font-weight:700;font-size:40px;color:var(--brand-blue);margin-top:10px;line-height:44px}
  .tagline{font-size:19px;color:var(--ink-grey);margin-top:10px}
  .tab{position:absolute;height:31px;line-height:31px;font-size:17px;color:var(--white)}
  .tab-advisor{left:0;top:506px;width:245px;padding-left:18px;background:var(--brand-blue);clip-path:polygon(0 0,96% 0,100% 100%,0 100%)}
  .tab-project{left:158px;top:680px;width:246px;padding-left:52px;background:var(--tab-grey);clip-path:polygon(2% 0,100% 0,100% 100%,0 100%)}
  .feature-row{position:absolute;left:0;width:404px;display:flex;justify-content:space-around;padding:0 14px}
  .feature{width:120px;text-align:center;font-size:11.5px;line-height:14px;color:var(--brand-blue)}
  .feature-icon{width:56px;height:56px;border-radius:50%;margin:0 auto 12px}
  .icon-teal{background:var(--teal)}
  .icon-outline{background:var(--white);border:1.5px solid var(--brand-blue)}
  .row-advisor{top:561px}
  .row-project{top:739px}
  .footer-wave{position:absolute;left:0;top:835px;width:404px;height:116px}
  .site{position:absolute;left:0;width:404px;top:882px;text-align:center;color:var(--white);font-size:19px}
  .site svg{vertical-align:-3px;margin-right:10px}
</style>
</head>
<body>
<main class="banner">
  <div class="hero-photo" role="img" aria-label="Photo of a smiling woman looking at her smartphone against a warm blurred city-light background"></div>
  <svg class="hero-curve" viewBox="0 0 404 80" aria-hidden="true">
    <path d="M0 80 L0 48 Q202 0 404 48 L404 80 Z" fill="var(--curve-grey)"/>
    <path d="M0 80 L0 56 Q202 8 404 56 L404 80 Z" fill="var(--paper)"/>
  </svg>
  <h1 class="headline">Brivanta<br>matches you with<br>the right advisors<br>online!</h1>

  <div class="brand">
    <div class="brand-dot"></div>
    <div class="brand-name">Brivanta</div>
    <p class="tagline">We’ll Find the Best Advisors for You!</p>
  </div>

  <div class="tab tab-advisor">Looking for an advisor?</div>
  <div class="feature-row row-advisor">
    <div class="feature"><div class="feature-icon icon-teal" role="img" aria-label="Online marketplace storefront icon"></div>One-stop borderless<br>marketplace</div>
    <div class="feature"><div class="feature-icon icon-teal" role="img" aria-label="Running figure icon"></div>Convenient and<br>quick</div>
    <div class="feature"><div class="feature-icon icon-teal" role="img" aria-label="Thumbs up icon"></div>Hire with<br>confidence</div>
  </div>

  <div class="tab tab-project">Looking for a project?</div>
  <div class="feature-row row-project">
    <div class="feature"><div class="feature-icon icon-outline" role="img" aria-label="Profile card icon"></div>ProfessionalProfile</div>
    <div class="feature"><div class="feature-icon icon-outline" role="img" aria-label="Portfolio showcase icon"></div>Expertise Showcase</div>
    <div class="feature"><div class="feature-icon icon-outline" role="img" aria-label="Job leads tag icon"></div>Job Leads</div>
  </div>

  <svg class="footer-wave" viewBox="0 0 404 116" aria-hidden="true">
    <path d="M0 24 Q202 -10 404 24 L404 116 L0 116 Z" fill="var(--curve-grey)"/>
    <path d="M0 30 Q202 -4 404 30 L404 116 L0 116 Z" fill="var(--brand-blue)"/>
  </svg>
  <p class="site"><svg width="20" height="20" viewBox="0 0 20 20" aria-hidden="true"><circle cx="10" cy="10" r="8" fill="none" stroke="var(--white)" stroke-width="2"/><path d="M2 10h16M10 2c3 3 3 13 0 16M10 2c-3 3-3 13 0 16" fill="none" stroke="var(--white)" stroke-width="1.5"/></svg>www.brivanta.online</p>
</main>
</body>
</html>
```